Website redesign

Looking to redesign our existing website. (hire4ward.com.au)
New design needs to be bright, fun and have an easy flowing.
The website needs to be design with call to action.

Some examples of other websites:
brightdesk.com
lendnest.com.au

We are happy with the content of our existing website.

Target Market(s)

other businesses

Industry/Entity Type

Business Service

Number of Pages Required

5+ page

Requirements
Must have
• Theme redesign
Cool animation similar to brightdesk.com

```html
<!DOCTYPE html>
<html lang="en">
<head>
<meta charset="utf-8">
<title>Hire 4ward — Virtual Assistants</title>
<link href="https://fonts.googleapis.com/css2?family=Archivo:wght@400;500;600;700;800&family=Roboto:wght@400;500;700&display=swap" rel="stylesheet">
<style>
:root{
  --blue:#1a98dc;
  --blue-dark:#1486c6;
  --blue-soft:#5cbdea;
  --ink:#1b2733;
  --text:#2c3640;
  --muted:#5b6670;
  --pale:#e4eff9;
  --line:#8fa3b3;
  --white:#ffffff;
}
*{box-sizing:border-box;margin:0;padding:0}
html,body{width:1200px;height:4615px;overflow:hidden}
body{position:relative;background:var(--white);font-family:"Roboto",sans-serif;color:var(--text)}
.abs{position:absolute}
h1,h2,h3,h4{font-family:"Archivo",sans-serif;color:var(--ink)}
.rule{position:absolute;height:3px;width:46px;background:var(--blue)}

/* header */
.site-header{position:absolute;left:0;top:0;width:1200px;height:118px;background:var(--white)}
.brand{position:absolute;left:130px;top:26px;display:flex;align-items:center;gap:12px}
.brand-dot{width:30px;height:30px;border-radius:50%;background:var(--blue)}
.brand-name{font-family:"Archivo",sans-serif;font-weight:600;font-size:28px;color:var(--ink);letter-spacing:.5px}
.btn{display:inline-block;background:var(--blue);color:var(--white);font-family:"Archivo",sans-serif;font-weight:700;font-size:13px;text-transform:uppercase;border-radius:5px;text-align:center}
.header-quote{position:absolute;left:741px;top:25px;width:124px;height:35px;line-height:35px}
.call{position:absolute;left:887px;top:20px;display:flex;gap:12px;align-items:center}
.call small{display:block;font-size:13px;color:var(--ink)}
.call strong{display:block;font-family:"Archivo",sans-serif;font-size:21px;color:var(--blue);font-weight:600}
.nav{position:absolute;top:83px;left:565px;display:flex;gap:37px;font-family:"Archivo",sans-serif;font-weight:600;font-size:13px;color:var(--ink)}
.nav .active{color:var(--blue)}

/* hero */
.hero{position:absolute;left:0;top:118px;width:1200px;height:520px;overflow:hidden}
.hero-photo{position:absolute;left:0;top:0;width:760px;height:520px;background:linear-gradient(135deg,#7a7f6c,#b4b0a1 45%,#d9d6cf)}
.hero-panel{position:absolute;left:0;top:0}
.hero-title{position:absolute;left:836px;top:62px;font-size:45px;font-weight:800;line-height:1.1;color:var(--white)}
.hero-sub{position:absolute;left:836px;top:190px;font-size:21px;line-height:1.5;color:var(--white)}
.hero-btn{position:absolute;left:838px;top:288px;width:132px;height:38px;line-height:38px;background:var(--white);color:var(--blue);border-radius:5px}
.hero-arrows{position:absolute;left:1030px;top:440px}

/* services */
.services{position:absolute;left:0;top:638px;width:1200px;height:644px;overflow:hidden}
.services h2{position:absolute;left:129px;top:60px;font-size:23px;font-weight:700}
.services p{position:absolute;left:129px;top:128px;width:380px;font-size:16px;line-height:1.6;color:var(--text)}
.services-photo{position:absolute;left:-70px;top:232px;width:590px;height:560px;border-radius:50%;background:radial-gradient(circle at 45% 45%,#e9e4df,#d7e8f4 62%,#e1eef8)}
.services-bg{position:absolute;left:990px;top:-160px;width:320px;height:320px;border-radius:50%;background:#eaf4fb}
.card{position:absolute;width:218px;height:226px;background:var(--white);border-radius:4px;box-shadow:0 4px 18px rgba(20,60,100,.14);text-align:center;padding:0 24px}
.card svg{margin-top:40px}
.card h4{font-family:"Roboto",sans-serif;font-weight:500;font-size:12px;line-height:1.45;text-transform:uppercase;margin-top:26px;color:var(--ink)}

/* outsourcing */
.outsourcing{position:absolute;left:0;top:1282px;width:1200px;height:457px;background:var(--pale)}
.outsourcing h2{position:absolute;left:129px;top:68px;font-size:26px;font-weight:700;line-height:1.4}
.outsourcing p{position:absolute;left:129px;top:242px;width:340px;font-size:15px;line-height:1.55}
.video{position:absolute;left:555px;top:111px;width:512px;height:240px;background:linear-gradient(120deg,#2a2e32,#4a4f55 50%,#283039);display:flex;align-items:center;justify-content:center}
.play{width:42px;height:42px;border-radius:50%;background:var(--white);display:flex;align-items:center;justify-content:center}

/* process */
.process{position:absolute;left:0;top:1739px;width:1200px;height:1467px}
.process h2{position:absolute;left:0;width:1200px;text-align:center;top:56px;font-size:23px;font-weight:700}
.process-path{position:absolute;left:0;top:0}
.step-icon{position:absolute;width:172px;height:172px;border-radius:50%;background:#d6ecf8;display:flex;align-items:center;justify-content:center}
.step-icon span{width:150px;height:150px;border-radius:50%;background:var(--blue);display:flex;align-items:center;justify-content:center}
.step{position:absolute;width:440px}
.step h3{font-size:13px;font-weight:700;text-transform:uppercase;margin-bottom:14px}
.step p{font-size:12px;line-height:1.55;color:var(--text)}

/* why */
.why{position:absolute;left:0;top:3206px;width:1200px;height:543px;background:var(--pale);overflow:hidden}
.why h2{position:absolute;left:0;width:1200px;text-align:center;top:52px;font-size:24px;font-weight:700}
.why .lead{position:absolute;left:0;width:1200px;text-align:center;top:93px;font-size:16px;color:var(--text)}
.perk{position:absolute;width:68px;height:68px;border-radius:50%;background:var(--white);box-shadow:0 3px 12px rgba(20,60,100,.12);display:flex;align-items:center;justify-content:center}
.perk-label{position:absolute;font-size:14px;line-height:1.4;color:var(--ink);text-transform:uppercase}
.perk-label.right{text-align:right}
.why-center{position:absolute;left:517px;top:304px;width:180px;height:180px;border-radius:50%;border:12px solid var(--blue);display:flex;align-items:center;justify-content:center;font-family:"Archivo",sans-serif;font-weight:700;font-size:22px;color:var(--blue);text-align:center;line-height:1.1}

/* quote */
.quote{position:absolute;left:0;top:3749px;width:1200px;height:517px}
.quote-photo{position:absolute;inset:0;background:linear-gradient(110deg,#c9c2b9,#e8e6e3 40%,#f3f3f3 70%,#e9ecef)}
.quote-form{position:absolute;left:688px;top:62px;width:406px;height:407px;background:var(--white);padding:30px 32px}
.quote-form h2{font-size:23px;font-weight:700}
.quote-form p{font-size:13px;line-height:1.4;margin-top:14px;width:260px}
.field{position:absolute;border:1px solid #c3c9cf;font-size:12px;color:var(--muted);padding:12px 14px}
.submit{position:absolute;left:32px;top:342px;width:107px;height:38px;line-height:38px;font-size:16px;border-radius:2px}

/* footer */
.site-footer{position:absolute;left:0;top:4266px;width:1200px;height:349px;background:var(--blue);color:var(--white)}
.footer-brand{position:absolute;left:128px;top:94px;display:flex;align-items:center;gap:14px}
.footer-brand .brand-dot{background:var(--white)}
.footer-brand .brand-name{color:var(--white);font-size:32px}
.fcol{position:absolute;top:50px}
.fcol h4{color:var(--white);font-size:13px;font-weight:700;margin-bottom:24px}
.fcol ul{list-style:none;font-size:12px;line-height:20px;text-transform:uppercase;opacity:.92}
.fitem{display:flex;gap:12px;align-items:flex-start;font-size:12px;line-height:16px;margin-bottom:24px}
.fitem .ic{width:22px;height:22px;border-radius:50%;background:var(--white);flex:none;margin-top:4px}
.copyright{position:absolute;left:0;width:1200px;text-align:center;top:317px;font-size:10px;opacity:.9}
</style>
</head>
<body>

<header class="site-header">
  <div class="brand"><span class="brand-dot"></span><span class="brand-name">HIRE 4WARD</span></div>
  <a class="btn header-quote">Get a quote</a>
  <div class="call">
    <svg width="36" height="36" viewBox="0 0 36 36" fill="none" stroke="#1a98dc" stroke-width="2"><path d="M8 5l6 0 2 7-4 3c2 4 5 7 9 9l3-4 7 2v6c-15 1-24-9-23-23z"/><path d="M22 6a9 9 0 0 1 8 8M22 11a4 4 0 0 1 3 3"/></svg>
    <div><small>Call Us</small><strong>07 3000 4821</strong></div>
  </div>
  <nav class="nav"><span class="active">HOME</span><span>OUR STORY</span><span>TIPS AND TRICKS</span><span>CONTACT US</span><span>FAQ</span></nav>
</header>

<section class="hero">
  <div class="hero-photo" role="img" aria-label="Smiling woman with a headset working on a laptop at a desk"></div>
  <svg class="hero-panel" width="1200" height="520" viewBox="0 0 1200 520">
    <path d="M708 0H1200V520H760Z" fill="#1a98dc"/>
    <path d="M1200 250C1080 250 980 350 980 520H1200Z" fill="#5cbdea"/>
  </svg>
  <h1 class="hero-title">VIRTUAL<br>ASSISTANT?</h1>
  <p class="hero-sub">Full Time Virtual Assistant<br>Betrothed to your business!</p>
  <a class="btn hero-btn">Get a quote</a>
  <svg class="hero-arrows" width="90" height="30" viewBox="0 0 90 30" fill="none" stroke="#fff" stroke-width="2"><path d="M4 15h24M12 7l-8 8 8 8M58 15h24M74 7l8 8-8 8"/></svg>
</section>

<section class="services">
  <div class="services-bg"></div>
  <h2>OUR SERVICES</h2>
  <div class="rule" style="left:129px;top:96px"></div>
  <p>We'll help you save tens (or even hundreds!) of thousands of dollars per year. But what do WE actually do? GLAD YOU ASKED!</p>
  <div class="services-photo" role="img" aria-label="Woman on a video call with her remote team on a laptop"></div>

  <div class="card" style="left:605px;top:68px">
    <svg width="62" height="62" viewBox="0 0 62 62" fill="none" stroke="#1a98dc" stroke-width="2"><rect x="14" y="8" width="32" height="42" rx="2"/><circle cx="30" cy="22" r="5"/><path d="M22 34c2-5 14-5 16 0M20 40h20M20 45h14"/><path d="M42 42l8 8 4-4-8-8"/></svg>
    <h4>We recruit virtual assistants (a.k.a office legends!)</h4>
  </div>
  <div class="card" style="left:849px;top:93px">
    <svg width="62" height="62" viewBox="0 0 62 62" fill="none" stroke="#1a98dc" stroke-width="2.4"><path d="M14 36v-6a17 17 0 0 1 34 0v6"/><rect x="10" y="34" width="9" height="14" rx="3"/><rect x="43" y="34" width="9" height="14" rx="3"/></svg>
    <h4>Provide the tech support for these superheroes!</h4>
  </div>
  <div class="card" style="left:605px;top:319px">
    <svg width="62" height="62" viewBox="0 0 62 62" fill="none" stroke="#1a98dc" stroke-width="2"><path d="M16 10l8 0 3 10-5 4c3 6 7 10 13 13l4-5 10 3v8c-20 2-35-13-33-33z"/><path d="M34 12a14 14 0 0 1 13 13M34 19a7 7 0 0 1 6 6"/></svg>
    <h4>Set up the phone system (their own bat phone!)</h4>
  </div>
  <div class="card" style="left:849px;top:342px">
    <svg width="62" height="62" viewBox="0 0 62 62" fill="none" stroke="#1a98dc" stroke-width="2.2"><circle cx="31" cy="31" r="8"/><path d="M31 9v7M31 46v7M9 31h7M46 31h7M15 15l5 5M42 42l5 5M15 47l5-5M42 20l5-5"/><circle cx="31" cy="31" r="16"/></svg>
    <h4>We manage virtual assistants and keep them in tip-top shape!</h4>
  </div>
</section>

<section class="outsourcing">
  <h2>OUTSOURCING. A BIG WORD<br>THAT MEANS BIG THINGS<br>FOR YOUR BUSINESS.</h2>
  <div class="rule" style="left:129px;top:199px"></div>
  <p>Virtual Assistants are the superheroes of the modern office. They can do everything your team can do on a computer at a fraction of the price! (Well, maybe not high five you when you've had a win, but a virtual high five is definitely on the table!)</p>
  <div class="video" role="img" aria-label="Video still of the two company founders introducing the service">
    <span class="play"><svg width="16" height="18" viewBox="0 0 16 18"><path d="M2 1l13 8-13 8z" fill="#1a98dc"/></svg></span>
  </div>
</section>

<section class="process">
  <h2>THE PROCESS</h2>
  <div class="rule" style="left:577px;top:96px"></div>
  <svg class="process-path" width="1200" height="1467" viewBox="0 0 1200 1467" fill="none" stroke="#8fa3b3" stroke-width="1.5" stroke-dasharray="6 6">
    <path d="M889 335c0 40-20 55-70 55H320c-50 0-70 15-70 50"/>
    <path d="M250 610c0 40 20 55 70 55h490c50 0 80 15 80 45"/>
    <path d="M889 880c0 40-20 55-70 55H320c-50 0-70 15-70 50"/>
    <path d="M250 1150c0 40 20 55 70 55h490c50 0 80 15 80 45"/>
  </svg>

  <div class="step-icon" style="left:833px;top:163px"><span>
    <svg width="80" height="70" viewBox="0 0 80 70" fill="none" stroke="#fff" stroke-width="2.4"><rect x="6" y="8" width="68" height="44"/><circle cx="40" cy="26" r="9"/><path d="M34 34l-2 22 8-5 8 5-2-22M16 20h12M52 20h12M16 44h10"/></svg>
  </span></div>
  <div class="step" style="left:338px;top:210px"><h3>1. Provide your preferred qualifications.</h3><p>Set up a call with our team to specify the requirements and qualifications you're searching for in a Virtual Assistant. This will be our checklist for your perfect assistant! From there, we'll take care of shortlisting, testing, background checking and recruiting.</p></div>

  <div class="step-icon" style="left:167px;top:432px"><span>
    <svg width="76" height="66" viewBox="0 0 76 66" fill="none" stroke="#fff" stroke-width="2.4"><rect x="6" y="6" width="64" height="54" rx="3"/><path d="M6 16h64M14 24h14v14H14zM34 28h26M34 34h18M48 44h14v12H48zM14 46h28M14 52h20"/></svg>
  </span></div>
  <div class="step" style="left:433px;top:473px;width:470px"><h3>2. Endorsing the shortlisted candidates</h3><p>After the thorough vetting process, we'll put forward the best candidate. You can then conduct the final interview on your preferred communication platform at a time that suits you. Once the schedule is set, we'll let the candidates know!</p></div>

  <div class="step-icon" style="left:833px;top:709px"><span>
    <svg width="84" height="66" viewBox="0 0 84 66" fill="none" stroke="#fff" stroke-width="2.4"><circle cx="20" cy="14" r="7"/><circle cx="64" cy="14" r="7"/><path d="M8 50V34c0-7 5-10 12-10s10 4 12 8h20c2-4 5-8 12-8s12 3 12 10v16M28 36h28v6H28zM42 42v16M12 58h16M56 58h16"/></svg>
  </span></div>
  <div class="step" style="left:338px;top:741px"><h3>3. Conducting the final interview</h3><p>The final interview is the perfect time to get to know the candidates. It'll help to have a list of questions prepared that will help you pick out the chosen one!</p></div>

  <div class="step-icon" style="left:167px;top:974px"><span>
    <svg width="80" height="74" viewBox="0 0 80 74" fill="none" stroke="#fff" stroke-width="2.4"><rect x="6" y="6" width="68" height="48" rx="3"/><rect x="14" y="12" width="24" height="18"/><rect x="42" y="12" width="24" height="18"/><rect x="14" y="32" width="24" height="16"/><rect x="42" y="32" width="24" height="16"/><path d="M40 54v10M26 68h28"/></svg>
  </span></div>
  <div class="step" style="left:433px;top:1011px;width:360px"><h3>4. Setting up the tools</h3><p>Once you've chosen your Virtual Assistant, it's time for their system to be set up. You can get your own IT team onto the installation, otherwise, we've got a super team of tech peeps who can do it for you.</p></div>

  <div class="step-icon" style="left:833px;top:1247px"><span>
    <svg width="60" height="76" viewBox="0 0 60 76" fill="none" stroke="#fff" stroke-width="2.4"><path d="M30 4c10 10 14 22 12 40H18C16 26 20 14 30 4z"/><circle cx="30" cy="26" r="5"/><path d="M18 36l-10 12v8l10-6M42 36l10 12v8l-10-6M24 52v10M30 52v16M36 52v10"/></svg>
  </span></div>
  <div class="step" style="left:338px;top:1276px;width:410px"><h3>5. Your magical journey begins</h3><p>Now you and your Virtual Assistant are all set up and ready to rumble! Feel the magic of having a reliable assistant to take on all the menial, repetitive, time-consuming tasks, and focus your energy on more important things. Meet new clients, explore business opportunities, or just spend some time with friends and family!</p></div>
</section>

<section class="why">
  <h2>IT'S TIME TO HIRE 4WARD</h2>
  <p class="lead">Why are we your new best outsourcing friend?</p>
  <div class="rule" style="left:577px;top:132px"></div>
  <svg class="abs" style="left:0;top:0" width="1200" height="543" viewBox="0 0 1200 543"><circle cx="607" cy="394" r="180" fill="none" stroke="#cfe2f0" stroke-width="1.5"/></svg>
  <div class="why-center">HIRE<br>4WARD</div>

  <div class="perk" style="left:498px;top:195px"><svg width="30" height="30" viewBox="0 0 30 30" fill="none" stroke="#1a98dc" stroke-width="1.8"><rect x="6" y="3" width="18" height="24"/><path d="M10 20l10-10M11 11h.1M19 19h.1"/></svg></div>
  <span class="perk-label right" style="left:330px;top:221px;width:152px">No super or tax</span>
  <div class="perk" style="left:643px;top:199px"><svg width="30" height="30" viewBox="0 0 30 30" fill="none" stroke="#1a98dc" stroke-width="1.8"><rect x="4" y="9" width="22" height="16" rx="2"/><path d="M11 9V5h8v4M4 16h22M13 16v3h4v-3"/></svg></div>
  <span class="perk-label" style="left:733px;top:208px">Dedicated to your<br>business only</span>
  <div class="perk" style="left:408px;top:288px"><svg width="30" height="30" viewBox="0 0 30 30" fill="none" stroke="#1a98dc" stroke-width="1.8"><rect x="7" y="3" width="16" height="24"/><path d="M11 9h8M11 21h8M15 13v6"/></svg></div>
  <span class="perk-label right" style="left:240px;top:309px;width:156px">One invoice<br>per month</span>
  <div class="perk" style="left:736px;top:292px"><svg width="30" height="30" viewBox="0 0 30 30" fill="none" stroke="#1a98dc" stroke-width="1.8"><path d="M5 7h5l2 5-3 2c2 3 4 5 7 7l2-3 5 2v5C13 26 4 17 5 7z"/><path d="M17 4h10v7h-5l-3 2v-2h-2z"/></svg></div>
  <span class="perk-label" style="left:821px;top:311px">Dedicated<br>phone system</span>
  <div class="perk" style="left:401px;top:406px"><svg width="30" height="30" viewBox="0 0 30 30" fill="none" stroke="#1a98dc" stroke-width="1.8"><rect x="5" y="6" width="20" height="14" rx="1"/><circle cx="15" cy="12" r="3"/><path d="M10 18c2-3 8-3 10 0M2 24h26"/></svg></div>
  <span class="perk-label right" style="left:220px;top:433px;width:166px">Your own<br>virtual assistant</span>
  <div class="perk" style="left:747px;top:410px"><svg width="30" height="30" viewBox="0 0 30 30" fill="none" stroke="#1a98dc" stroke-width="2"><path d="M6 6l18 18M24 6L6 24M4 4l4 0 0 4M26 26l-4 0 0-4"/></svg></div>
  <span class="perk-label" style="left:827px;top:433px">IT setup and<br>support</span>
</section>

<section class="quote">
  <div class="quote-photo" role="img" aria-label="Man at a desk on a video conference with his team on a large monitor"></div>
  <form class="quote-form">
    <h2>GET A QUOTE</h2>
    <p>Fill in the form below to get a Quote for your own personal Virtual Assistant</p>
    <div class="field" style="left:32px;top:130px;width:166px;height:38px">Business Name</div>
    <div class="field" style="left:210px;top:130px;width:166px;height:38px">Full Name</div>
    <div class="field" style="left:32px;top:182px;width:166px;height:38px">Ph No.</div>
    <div class="field" style="left:210px;top:182px;width:166px;height:38px">E mail</div>
    <div class="field" style="left:32px;top:234px;width:344px;height:90px">Message</div>
    <span class="btn submit">SUBMIT</span>
  </form>
</section>

<footer class="site-footer">
  <div class="footer-brand"><span class="brand-dot"></span><span class="brand-name">HIRE 4WARD</span></div>
  <div class="fcol" style="left:513px">
    <h4>MENU</h4>
    <ul><li>Home</li><li>Our Story</li><li>Tips and Tricks</li><li>Contact Us</li><li>FAQ</li></ul>
  </div>
  <div class="fcol" style="left:700px">
    <h4>CONTACT US</h4>
    <div class="fitem"><span class="ic"></span><span>Call Us<br>0400 555 182</span></div>
    <div class="fitem"><span class="ic"></span><span>E mail Us<br>sam@hire4ward.com.au</span></div>
  </div>
  <div class="fcol" style="left:963px">
    <h4>FOLLOW US</h4>
    <div class="fitem"><span class="ic"></span><span>Like us on<br>CIRCLEFEED</span></div>
    <div class="fitem"><span class="ic"></span><span>Follow us on<br>CHIRPLINE</span></div>
    <div class="fitem"><span class="ic"></span><span>Follow us on<br>WORKLINK</span></div>
  </div>
  <p class="copyright">Copyright © 2020 All Rights Reserved</p>
</footer>

</body>
</html>
```